Website Design For Physical Therapy/Sports Massage Clinic

Hi! I am looking for a sleek, fun and functional new wordpress website for my physical therapy/sports massage clinic. My current site is www.velmoracarestudio.com. As you can see it's very basic and well... boring. :) In addition to a fun new look, I would also love this to be mobile friendly.

In terms of add on services/widgets I would like to use Brindle Booking + Quill Consent so that people can schedule and fill out paperwork remotely. Both seem like easy add ons to any site, but just in case here are the sites for both to ensure compatibility with the new design.

https://secure.brindlebooking.com/
https://www.quillconsent.com/

Thanks for reading and I'm excited to get started. I would love to see designs that are modern, athlete minded and fun as those are my clients. Attached you will find two logos (one white and one blue).

Target Market(s)

Athletes and weekend warriors

Industry/Entity Type

Physical Therapy

Number of Pages Required

1 page

Font styles to use
Sans Serif

Requirements
Must have
• 1) A fun home page that is modern and easy to navigate and 2) a website that is compatible with Brindle booking + quill consent so that my patients can schedule and fill out their paperwork without me.

```html
<!DOCTYPE html>
<html lang="en">
<head>
<meta charset="utf-8">
<title>Velmora Care Studio — Sports Therapy</title>
<link rel="stylesheet" href="https://fonts.googleapis.com/css2?family=Open+Sans:ital,wght@0,400;0,600;0,700;1,400&family=Roboto:wght@400;500;700&display=swap">
<style>
:root{
  --navy:#0d3a66;
  --navy-dark:#0a2b4c;
  --nav-top:#2262a3;
  --nav-bottom:#164a80;
  --orange:#e0611b;
  --text:#333a40;
  --muted:#6b7280;
  --grey-bg:#efefef;
  --line:#d8d8d8;
  --white:#ffffff;
  --contact-bg:#1b2636;
  --footer-bg:#0e2a48;
}
*{box-sizing:border-box;margin:0;padding:0}
html,body{width:1200px;height:3543px;overflow:hidden}
body{position:relative;background:var(--white);font-family:"Open Sans",Arial,sans-serif;color:var(--text)}
.abs{position:absolute}
h2.section-title{position:absolute;left:0;width:1200px;text-align:center;font-family:"Roboto",Arial,sans-serif;font-weight:400;font-size:34px;color:var(--navy);letter-spacing:.5px}
.title-rule{position:absolute;left:500px;width:200px;height:20px}
.title-rule::before,.title-rule::after{content:"";position:absolute;top:9px;width:78px;height:2px;background:var(--navy)}
.title-rule::before{left:0}.title-rule::after{right:0}
.title-rule span{position:absolute;left:92px;top:3px;width:16px;height:16px;border-radius:50%;background:var(--orange)}

/* header */
.top-line{top:0;left:0;width:1200px;height:5px;background:var(--navy)}
.brand{top:42px;left:98px;display:flex;align-items:center;gap:12px}
.brand-mark{width:34px;height:34px;background:var(--orange)}
.brand-name{font-weight:700;font-size:26px;color:var(--navy);line-height:1}
.phone{top:58px;left:622px;display:flex;align-items:center;gap:10px;font-size:17px;color:var(--navy)}
.phone-icon{width:30px;height:30px;border:2px solid var(--orange);border-radius:50%;display:flex;align-items:center;justify-content:center}
.search{top:56px;left:810px;width:290px;height:40px;border:1px solid var(--line);display:flex}
.search-field{flex:1;padding:0 12px;font-size:12px;color:var(--muted);line-height:38px}
.search-btn{width:42px;background:var(--orange);display:flex;align-items:center;justify-content:center}
.main-nav{top:146px;left:0;width:1200px;height:59px;background:linear-gradient(var(--nav-top),var(--nav-bottom))}
.main-nav ul{list-style:none;display:flex;height:100%;padding-left:98px}
.main-nav li{width:137px;text-align:center;line-height:59px;font-family:"Roboto",Arial,sans-serif;font-size:14px;color:var(--white);text-transform:uppercase}
.main-nav li.active{background:var(--orange)}

/* hero */
.hero{top:205px;left:0;width:1200px;height:461px;background:linear-gradient(90deg,#cfc9c2 0%,#e8e4df 35%,#f4f3f1 60%,#fafafa 100%)}
.hero-brand{top:310px;left:645px;display:flex;align-items:center;gap:12px}
.hero-brand .brand-name{font-size:28px}
.hero-text{top:418px;left:645px;width:480px;font-size:14px;line-height:22px;color:var(--navy)}
.btn-orange{background:var(--orange);color:var(--white);font-size:13px;text-align:center}
.hero-btn{top:472px;left:645px;width:150px;height:48px;line-height:48px}
.hero-arrow{top:380px;width:20px;height:56px}

/* welcome */
.welcome-title{top:740px;left:99px;font-family:"Roboto",Arial,sans-serif;font-size:33px;font-weight:400;color:var(--navy)}
.welcome-rule{top:786px;left:99px;width:460px;height:2px;background:var(--navy)}
.welcome-text{top:818px;left:99px;width:665px;font-size:12.5px;line-height:23px;color:var(--text)}
.btn-navy{background:var(--navy);color:var(--white);font-size:13px;text-align:center}
.welcome-btn{top:973px;left:99px;width:148px;height:46px;line-height:46px}
.welcome-photo{top:709px;left:780px;width:420px;height:366px;background:radial-gradient(ellipse at 60% 45%,#d76fb6 0%,#e9a7d3 30%,#ffffff 65%)}

/* services */
.services{top:1075px;left:0;width:1200px;height:500px;background:var(--grey-bg)}
.service-card{top:1299px;width:308px;height:232px;background:var(--white);border:1px solid var(--line);text-align:center;padding:112px 22px 0}
.card-title{font-family:"Roboto",Arial,sans-serif;font-size:14px;font-weight:500;color:#222;text-transform:uppercase;margin-bottom:6px}
.card-text{font-size:12.5px;line-height:19px;color:var(--text)}
.round-photo{border-radius:50%;border:8px solid var(--white);box-shadow:0 0 0 1px var(--line),0 6px 10px rgba(0,0,0,.12)}
.service-photo{top:1209px;width:186px;height:186px}
.slider-dot{top:1368px;width:28px;height:28px;border-radius:50%;background:#c8c8c8}

/* widgets */
.widget-photo{top:1712px;width:226px;height:226px}
.widget-title{top:1745px;font-family:"Roboto",Arial,sans-serif;font-size:19px;font-weight:700;color:#222;text-transform:uppercase}
.widget-text{top:1780px;width:250px;font-size:12.5px;line-height:25px;color:var(--text)}

/* testimonials */
.testimonials{top:1996px;left:0;width:1200px;height:420px;background:var(--grey-bg)}
.testimonial-photo{top:2154px;left:200px;width:156px;height:156px;background:radial-gradient(circle,#b98a6a,#6e4a34)}
.quote-mark{top:2178px;left:412px;font-size:44px;color:#b7b7b7;font-family:Georgia,serif}
.quote{top:2196px;left:432px;width:650px;font-style:italic;font-size:12.5px;line-height:22px;color:#555}
.quote-name{top:2276px;left:432px;font-family:"Roboto",Arial,sans-serif;font-size:12px;font-weight:700;color:var(--navy);text-transform:uppercase}
.quote-handle{top:2298px;left:432px;font-size:11px;color:#555}
.dots{top:2288px;left:1070px;display:flex;gap:5px}
.dots span{width:9px;height:9px;border-radius:50%}

/* blog */
.blog-card{top:2664px;width:296px;height:266px;background:var(--white);border:1px solid var(--line);padding:96px 22px 0}
.blog-photo{top:2558px;width:188px;height:188px}
.blog-text{font-size:12.5px;line-height:19px;color:var(--text);text-align:justify}
.blog-meta{position:absolute;bottom:14px;left:22px;right:22px;display:flex;justify-content:space-between;font-size:10.5px;color:#555}

/* contact */
.contact{top:2971px;left:0;width:1200px;height:525px;background:linear-gradient(90deg,#1c2737,#243349 60%,#1a2434)}
.contact .section-title{color:var(--white)}
.contact .title-rule::before,.contact .title-rule::after{background:var(--white)}
.field{left:87px;width:402px;height:40px;background:var(--white);border:1px solid #cfd4da;display:flex;align-items:center;gap:12px;padding:0 14px;font-size:12px;color:#666}
.field-message{align-items:flex-start;padding-top:12px}
.submit{top:3397px;left:85px;width:162px;height:44px;line-height:44px;background:var(--navy);color:var(--white);font-size:13px;text-align:center}
.map{top:3108px;left:522px;width:364px;height:270px;border:4px solid var(--white);background:linear-gradient(135deg,#d9dcd5,#c9d3c4 50%,#dcdad0)}
.map-label{top:3120px;left:690px;width:130px;padding:8px;background:var(--navy);color:var(--white);font-size:11px;line-height:15px}
.info-title{top:3118px;left:909px;font-family:"Roboto",Arial,sans-serif;font-size:20px;font-weight:700;color:var(--white);text-transform:uppercase}
.info-row{left:909px;display:flex;gap:14px;color:var(--white);font-size:12.5px;line-height:18px}
.info-row svg{flex:none;margin-top:2px}

/* footer */
.footer{top:3496px;left:0;width:1200px;height:47px;background:var(--footer-bg)}
.copyright{top:3512px;left:87px;font-size:12px;color:var(--white)}
.socials{top:3506px;left:940px;display:flex;gap:9px}
.socials span{width:28px;height:28px;border-radius:50%;border:1.5px solid var(--white)}
</style>
</head>
<body>

<!-- header -->
<div class="abs top-line"></div>
<div class="abs brand"><span class="brand-mark"></span><span class="brand-name">Velmora Care Studio</span></div>
<div class="abs phone">
  <span class="phone-icon"><svg width="14" height="14" viewBox="0 0 24 24"><path fill="#e0611b" d="M6.6 10.8a15.2 15.2 0 0 0 6.6 6.6l2.2-2.2a1 1 0 0 1 1-.25 11.4 11.4 0 0 0 3.6.57 1 1 0 0 1 1 1V20a1 1 0 0 1-1 1A17 17 0 0 1 3 4a1 1 0 0 1 1-1h3.5a1 1 0 0 1 1 1c0 1.25.2 2.45.57 3.57a1 1 0 0 1-.25 1z"/></svg></span>
  555-301-4182
</div>
<div class="abs search">
  <div class="search-field">Enter your keywords...</div>
  <div class="search-btn"><svg width="16" height="16" viewBox="0 0 24 24"><circle cx="10" cy="10" r="6.5" fill="none" stroke="#fff" stroke-width="3"/><line x1="15" y1="15" x2="21" y2="21" stroke="#fff" stroke-width="3"/></svg></div>
</div>
<nav class="abs main-nav">
  <ul>
    <li class="active">Home</li><li>About</li><li>Services</li><li>New Patients</li><li>Pricing</li><li>Contact Us</li><li>Blog</li>
  </ul>
</nav>

<!-- hero -->
<section class="abs hero" role="img" aria-label="Therapist treating a patient's back on a treatment table"></section>
<svg class="abs hero-arrow" style="left:16px" viewBox="0 0 20 56"><polyline points="18,2 3,28 18,54" fill="none" stroke="#fff" stroke-width="2"/></svg>
<svg class="abs hero-arrow" style="left:1140px" viewBox="0 0 20 56"><polyline points="2,2 17,28 2,54" fill="none" stroke="#777" stroke-width="2"/></svg>
<div class="abs hero-brand"><span class="brand-mark"></span><span class="brand-name">Velmora Care Studio</span></div>
<p class="abs hero-text">Velmora Care Studio offers comprehensive, results-driven rehabilitation and performance programs for active individuals</p>
<div class="abs btn-orange hero-btn">View more info</div>

<!-- welcome -->
<h1 class="abs welcome-title">WELCOME TO SPORTS THERAPY</h1>
<div class="abs welcome-rule"></div>
<p class="abs welcome-text">Velmora Care Studio is not your average Physical Therapy clinic. Here you will never find a room full of patients working out simultaneously. Nor will you experience a visit that consists solely of modalities and exercise; instead, you will find effective, 1-on-1 care that delivers the skilled hands on/manual therapy that you need.Upon starting treatment, you will first undergo a thorough evaluation to determine not only your diagnosis, but also the causes behind it. What breaks and why are rarely the same and a comprehensive, full body approach will be used to identify contributing factors such as mobility, strength, posture, and bio-mechanics/sports technique</p>
<div class="abs btn-navy welcome-btn">View more info</div>
<div class="abs welcome-photo" role="img" aria-label="Man in a pink shirt holding his lower back"></div>

<!-- services -->
<section class="abs services"></section>
<h2 class="section-title" style="top:1124px">OUR SERVICES</h2>
<div class="title-rule" style="top:1170px"><span></span></div>
<div class="abs slider-dot" style="left:29px"></div>
<div class="abs slider-dot" style="left:1143px"></div>

<div class="abs service-card" style="left:94px"><div class="card-title">Quality Hands On Time</div><p class="card-text">Velmora Care Studio has one goal: to get you back to what you love doing as fast as possible.</p></div>
<div class="abs service-card" style="left:444px"><div class="card-title">Effective Treatments</div><p class="card-text">Treatment techniques used at Velmora Care Studio include: Deep Tissue Release, Tool-Assisted Technique (instrument assisted soft tissue mobilization),</p></div>
<div class="abs service-card" style="left:791px"><div class="card-title">Education</div><p class="card-text">Battling an injury with a big race or competition looming? Velmora Care Studio can help. Not only will you be taught ways to modify</p></div>
<div class="abs round-photo service-photo" style="left:155px;background:radial-gradient(circle,#e8b9a0,#b06d53)" role="img" aria-label="Hands massaging a shoulder"></div>
<div class="abs round-photo service-photo" style="left:505px;background:radial-gradient(circle,#f07aa8 0%,#e9c3a8 45%,#f3ece6)" role="img" aria-label="Knee with pink kinesiology tape"></div>
<div class="abs round-photo service-photo" style="left:852px;background:radial-gradient(circle at 60% 40%,#e85b3c 0%,#2b5a9a 35%,#0b1c3a)" role="img" aria-label="Anatomical view of a knee joint"></div>

<!-- widgets -->
<h2 class="section-title" style="top:1614px">OUR WIDGETS</h2>
<div class="title-rule" style="top:1660px"><span></span></div>
<div class="abs round-photo widget-photo" style="left:94px;background:linear-gradient(135deg,#2e7a78,#e9e3d6 70%)" role="img" aria-label="Brindle Booking scheduling screen"></div>
<div class="abs widget-title" style="left:342px">Brindle Booking</div>
<p class="abs widget-text" style="left:342px">Clients can see your real-time calendar availability, self-select the time that works best for them, and easily book (and pay for!) their own appointments in advance, sparing you 89%*</p>
<div class="abs round-photo widget-photo" style="left:609px;background:linear-gradient(180deg,#f4f4f4,#e6d3b8 60%,#c9935a)" role="img" aria-label="Quill Consent waiver screen"></div>
<div class="abs widget-title" style="left:855px">Quill Consent</div>
<p class="abs widget-text" style="left:855px">Clients can see your real-time calendar availability, self-select the time that works best for them, and easily book (and pay for!) their own appointments in advance, sparing you 89%*</p>

<!-- testimonials -->
<section class="abs testimonials"></section>
<h2 class="section-title" style="top:2066px">TESTIMONIALS</h2>
<div class="title-rule" style="top:2110px"><span></span></div>
<div class="abs round-photo testimonial-photo" role="img" aria-label="Portrait of the client"></div>
<div class="abs quote-mark">&ldquo;</div>
<p class="abs quote">As a tennis player turned fashion blogger/lawyer my lifestyle takes its toll.The Northgate Health Centre always take great care of me through osteopathy, acupuncture and exercise. I would recommend them to anyone looking for pain relief.&rdquo;</p>
<div class="abs quote-name">Marissa Kell</div>
<div class="abs quote-handle">mkell</div>
<div class="abs dots"><span style="background:#c0392b"></span><span style="background:var(--navy)"></span><span style="background:#7f8c9a"></span></div>

<!-- blog -->
<h2 class="section-title" style="top:2462px">OUR BLOG</h2>
<div class="title-rule" style="top:2508px"><span></span></div>

<article class="abs blog-card" style="left:99px"><div class="card-title" style="text-align:left">Quality Hands On Time</div><p class="blog-text">Velmora Care Studio is not your average Physical Therapy clinic. Here you will never find a room full of patients working out simultaneously. Nor will you experience a visit that consists solely</p><div class="blog-meta"><span>&#9719; 27 MARCH 2016</span><span>&#9632; 120</span><span>&#9829; 203</span></div></article>
<article class="abs blog-card" style="left:449px"><div class="card-title" style="text-align:left">Effective Treatments</div><p class="blog-text">Velmora Care Studio is not your average Physical Therapy clinic. Here you will never find a room full of patients working out simultaneously. Nor will you experience a visit that consists solely</p><div class="blog-meta"><span>&#9719; 27 MARCH 2016</span><span>&#9632; 120</span><span>&#9829; 203</span></div></article>
<article class="abs blog-card" style="left:803px"><div class="card-title" style="text-align:left">Battling an Injury</div><p class="blog-text">Velmora Care Studio is not your average Physical Therapy clinic. Here you will never find a room full of patients working out simultaneously. Nor will you experience a visit that consists solely</p><div class="blog-meta"><span>&#9719; 27 MARCH 2016</span><span>&#9632; 120</span><span>&#9829; 203</span></div></article>
<div class="abs round-photo blog-photo" style="left:153px;background:radial-gradient(circle,#e6b89e,#a8674c)" role="img" aria-label="Back massage"></div>
<div class="abs round-photo blog-photo" style="left:503px;background:radial-gradient(circle,#e2c0a6,#7c5a44)" role="img" aria-label="Leg being stretched by a therapist"></div>
<div class="abs round-photo blog-photo" style="left:857px;background:radial-gradient(circle,#d9d6d1,#8e8a84)" role="img" aria-label="Therapist assisting a patient's knee exercise"></div>

<!-- contact -->
<section class="abs contact">
  <h2 class="section-title" style="top:68px">CONTACT US</h2>
  <div class="title-rule" style="top:112px"><span></span></div>
</section>
<div class="abs field" style="top:3106px"><svg width="14" height="14" viewBox="0 0 24 24"><circle cx="12" cy="7" r="5" fill="#777"/><path d="M3 23c0-6 4-9 9-9s9 3 9 9z" fill="#777"/></svg>Your name</div>
<div class="abs field" style="top:3164px"><svg width="15" height="12" viewBox="0 0 24 18"><rect width="24" height="18" fill="#777"/><polyline points="1,1 12,10 23,1" fill="none" stroke="#fff" stroke-width="2"/></svg>Email address</div>
<div class="abs field" style="top:3220px"><svg width="12" height="14" viewBox="0 0 20 24"><path d="M0 0h13l7 7v17H0z" fill="#777"/></svg>Subject</div>
<div class="abs field field-message" style="top:3276px;height:102px"><svg width="14" height="14" viewBox="0 0 24 24"><path d="M3 21l1-5L16 4l4 4L8 20z" fill="#777"/></svg>Message</div>
<div class="abs submit">Submit</div>
<div class="abs map" role="img" aria-label="Street map showing the clinic location"></div>
<svg class="abs" style="top:3148px;left:668px" width="18" height="24" viewBox="0 0 18 24"><path d="M9 0a9 9 0 0 1 9 9c0 7-9 15-9 15S0 16 0 9a9 9 0 0 1 9-9z" fill="#d8362b"/><circle cx="9" cy="9" r="3.5" fill="#fff"/></svg>
<div class="abs map-label">Velmora Care Studio<br>2190 Larkfield Rd, Ste 310</div>
<div class="abs info-title">Contact Info</div>
<div class="abs info-row" style="top:3160px"><svg width="14" height="18" viewBox="0 0 18 24"><path d="M9 0a9 9 0 0 1 9 9c0 7-9 15-9 15S0 16 0 9a9 9 0 0 1 9-9z" fill="#fff"/><circle cx="9" cy="9" r="3.5" fill="#1c2737"/></svg><span>Velmora Care Studio<br>2190 Larkfield Rd, Ste 310<br>Hollin Creek, TX 78000</span></div>
<div class="abs info-row" style="top:3236px;font-size:15px"><svg width="16" height="16" viewBox="0 0 24 24"><path fill="#fff" d="M6.6 10.8a15.2 15.2 0 0 0 6.6 6.6l2.2-2.2a1 1 0 0 1 1-.25 11.4 11.4 0 0 0 3.6.57 1 1 0 0 1 1 1V20a1 1 0 0 1-1 1A17 17 0 0 1 3 4a1 1 0 0 1 1-1h3.5a1 1 0 0 1 1 1c0 1.25.2 2.45.57 3.57a1 1 0 0 1-.25 1z"/></svg><span>555 274-6130</span></div>
<div class="abs info-row" style="top:3282px;font-size:15px"><svg width="16" height="16" viewBox="0 0 24 24"><rect x="4" y="2" width="16" height="8" fill="#fff"/><rect x="1" y="9" width="22" height="9" rx="2" fill="#fff"/><rect x="5" y="14" width="14" height="8" fill="#fff" stroke="#1c2737" stroke-width="1.5"/></svg><span>555-619-2047</span></div>
<div class="abs info-row" style="top:3326px"><svg width="16" height="16" viewBox="0 0 24 24"><circle cx="12" cy="12" r="10" fill="none" stroke="#fff" stroke-width="2.5"/><polyline points="12,6 12,12 16,14" fill="none" stroke="#fff" stroke-width="2.5"/></svg><span>Open M-F. Please call or use the<br>contact form to schedule your<br>appointment!</span></div>

<!-- footer -->
<footer class="abs footer"></footer>
<div class="abs copyright">Copyright &copy; 2016 Velmora Care Studio. All Rights Reserved</div>
<div class="abs socials"><span></span><span></span><span></span><span></span><span></span></div>

</body>
</html>
```